New Business Card & Logo Design Project for PR Agency

Halvery & Partners Tech Public Relations agency is looking for a new business card design. Please see our website at www.halvery-pr.example for a description of our services. The design does not necessarily have to match the website’s aesthetic as we are looking for something fresh and modern that reflects our business. We want to emphasize that our focus is on media & public relations, content creation, social media and SEO. We want the business card to convey our BtoB technology focus and should have a very clean look. You are welcome to draw from our current halvery & partners logo on the card or play with that design too. We also like the idea of utilizing blue and white, which are often used in technology-related designs and layouts.
Attached are jpegs of the current logo and current card design for your reference.
Target Market(s)
Our clients are Business-to-Business technology providers.We sell our services to the CEO/President/Marketing director of a technology providing company.
Industry/Entity Type
Business
Look and feel

```html
<!DOCTYPE html>
<html lang="en">
<head>
<meta charset="utf-8">
<title>Halvery &amp; Partners — Business Card</title>
<link rel="stylesheet" href="https://fonts.googleapis.com/css2?family=EB+Garamond:ital,wght@0,500;0,700;1,600;1,700&display=swap">
<style>
  :root {
    --ink: #58585a;
    --pale-blue: #cdedfb;
    --pale-blue-soft: #e6f6fd;
    --paper: #ffffff;
  }
  * { margin: 0; padding: 0; box-sizing: border-box; }
  html, body {
    width: 1200px;
    height: 686px;
    overflow: hidden;
    background: var(--paper);
  }
  .card {
    position: relative;
    width: 1200px;
    height: 686px;
    background: var(--paper);
    font-family: "EB Garamond", Georgia, serif;
    color: var(--ink);
    overflow: hidden;
  }
  .ornament-area {
    position: absolute;
    left: 440px;
    top: 0;
    width: 760px;
    height: 686px;
  }
  .brand {
    position: absolute;
    left: 50px;
    top: 72px;
  }
  .brand-name {
    font-size: 64px;
    font-weight: 700;
    line-height: 1;
    letter-spacing: 0.2px;
  }
  .brand-tagline {
    margin-top: 6px;
    font-size: 29px;
    font-style: italic;
    font-weight: 700;
    line-height: 1;
  }
  .contact-left {
    position: absolute;
    right: 560px;
    top: 345px;
    text-align: right;
  }
  .contact-right {
    position: absolute;
    left: 686px;
    top: 345px;
  }
  .person-name {
    font-size: 73px;
    font-weight: 700;
    line-height: 1;
    white-space: nowrap;
  }
  .person-title {
    font-size: 40px;
    font-style: italic;
    font-weight: 700;
    line-height: 1;
    margin-top: 22px;
    margin-bottom: 24px;
  }
  .detail-list {
    list-style: none;
    font-size: 40px;
    font-weight: 700;
    line-height: 57px;
    white-space: nowrap;
  }
  .contact-left .detail-list { margin-top: 16px; }
  .contact-left .detail-list li:last-child { font-weight: 500; }
</style>
</head>
<body>
  <div class="card">
    <svg class="ornament-area" role="img" aria-label="Large pale blue brush-textured ornament" viewBox="0 0 760 686">
      <defs>
        <radialGradient id="ornament-glow" cx="55%" cy="55%" r="60%">
          <stop offset="0%" stop-color="var(--pale-blue)"/>
          <stop offset="100%" stop-color="var(--pale-blue-soft)" stop-opacity="0"/>
        </radialGradient>
      </defs>
      <rect width="760" height="686" fill="url(#ornament-glow)"/>
    </svg>

    <header class="brand">
      <div class="brand-name">halvery &amp; partners</div>
      <div class="brand-tagline">a public relations company</div>
    </header>

    <section class="contact-left">
      <h1 class="person-name">Daniel Morrow</h1>
      <ul class="detail-list">
        <li>dmorrow@halvery-pr.example</li>
        <li>halvery-pr.example</li>
        <li>(203) 555-0147</li>
      </ul>
    </section>

    <section class="contact-right">
      <p class="person-title">Partner</p>
      <ul class="detail-list">
        <li>48 Harbor Lane</li>
        <li>Suite 7</li>
        <li>Milford CT 06460</li>
      </ul>
    </section>
  </div>
</body>
</html>
```